Harlow Ridge Growers and Nursery needs a business street sign.

I have three businesses located at the same address: The Harlow Ridge Growers & Nursery, The Bramble Nook, and The Quarry Commons. I am looking for a 4’ x 8’ street sign to represent all three businesses as one retail experience. It needs to be eye catching yet simple enough that people can fully read it while driving by. I have logos for the greenhouse and village however I do not have anything for The Bramble Nook. I’m looking for some type of font that’s similar or in between the two attached logos for The Bramble Nook.

• Horizontal Sign, Eye catching, yet simple design so people see it while driving by.
• Horizontal Sign
• I’m open to the design being both vertical and horizontal. Please provide both options

```html
<!DOCTYPE html>
<html lang="en">
<head>
<meta charset="utf-8">
<title>Harlow Ridge Growers and Nursery – Street Sign</title>
<link rel="stylesheet" href="https://fonts.googleapis.com/css2?family=League+Spartan:wght@700;800&display=swap">
<style>
  :root {
    --page: #ffffff;
    --sign-light: #eafdf0;
    --sign-mid: #8ee8b0;
    --sign-edge: #44c08a;
    --green-deep: #0d4a25;
    --maroon: #7a2c34;
    --divider: rgba(60, 90, 70, 0.45);
    --grass-dark: #2f8a1e;
    --grass-light: #6fd13f;
    --cloud: #ffffff;
  }
  * { box-sizing: border-box; margin: 0; padding: 0; }
  html, body {
    width: 724px; height: 1200px; overflow: hidden;
    background: var(--page);
  }
  .street-sign {
    position: absolute; left: 22px; top: 430px;
    width: 680px; height: 340px; overflow: hidden;
    background:
      radial-gradient(ellipse 55% 60% at 50% 62%, var(--sign-light) 0%, rgba(234,253,240,0) 100%),
      linear-gradient(100deg, var(--sign-mid) 0%, #9bedbb 45%, #7ee0a7 75%, var(--sign-edge) 100%);
    box-shadow: 6px 8px 14px rgba(0,0,0,0.28);
    font-family: "League Spartan", "Futura", sans-serif;
  }
  .brand-row {
    position: absolute; top: 28px; left: 80px; width: 530px; height: 62px;
    display: flex; align-items: center;
  }
  .brand {
    font-weight: 700; line-height: 1.05; text-align: center;
    display: flex; align-items: center; justify-content: center;
  }
  .brand--growers { width: 160px; font-size: 14px; color: var(--green-deep); }
  .brand--commons { width: 180px; font-size: 19px; color: var(--maroon); }
  .brand--nook { width: 170px; font-size: 19px; color: var(--green-deep); }
  .brand-divider {
    width: 1px; height: 62px; background: var(--divider);
  }
  .cloud {
    position: absolute;
    background: radial-gradient(ellipse at 50% 55%, var(--cloud) 0%, rgba(255,255,255,0.75) 40%, rgba(255,255,255,0) 72%);
  }
  .cloud--left { left: 6px; top: 90px; width: 82px; height: 38px; }
  .cloud--right { left: 548px; top: 188px; width: 135px; height: 62px; }
  .headline {
    position: absolute; left: 0; width: 100%; text-align: center;
    font-weight: 800; text-transform: uppercase;
  }
  .headline__lead {
    top: 124px; font-size: 58px; line-height: 1; letter-spacing: 0.5px;
    color: var(--green-deep);
  }
  .headline__grow {
    top: 178px; font-size: 96px; line-height: 1; letter-spacing: 1px;
    color: var(--maroon);
  }
  .meadow {
    position: absolute; left: 37px; top: 246px; width: 608px; height: 94px;
    background: linear-gradient(180deg, rgba(111,209,63,0) 0%, var(--grass-light) 30%, var(--grass-dark) 100%);
    border-radius: 50% 50% 0 0 / 30% 30% 0 0;
  }
</style>
</head>
<body>
  <section class="street-sign">
    <div class="brand-row">
      <div class="brand brand--growers">The Harlow Ridge Growers &amp; Nursery</div>
      <div class="brand-divider"></div>
      <div class="brand brand--commons">The Quarry Commons</div>
      <div class="brand-divider"></div>
      <div class="brand brand--nook">The Bramble Nook</div>
    </div>

    <div class="cloud cloud--left" role="img" aria-label="Small white cloud"></div>
    <div class="cloud cloud--right" role="img" aria-label="White cloud"></div>

    <p class="headline headline__lead">Where Beauty</p>
    <p class="headline headline__grow">Grows</p>

    <div class="meadow" role="img" aria-label="Green grass with small white flowers along the bottom of the sign"></div>
  </section>
</body>
</html>
```